Harold The Realtor Business Card Design

I need a new card design for my real estate business in Seattle Wa. I am interested in a unique design. My business revolves around my personal services and I want the card to show professionalism, creativity and good execution. I specialize in residential real estate in Maple ridge / downtown neighborhoods. The card is my first impression on may of my clients and in the service industry any time you can stand out from the crowd and make an impression will go a long way.

Target Market(s)

I will be handing the card to prospects/ potential buyers and sellers of residential real estate.

Industry/Entity Type

Real Estate Agent

Contact Information for Business Card

Email: Info@Haroldtherealtor.com Website: HaroldtheRealtor.com Cell phone: 206-555-0184 Fax 206-555-0127

Font styles to use
Sans Serif

Colors
0255a3
ffc214

Requirements
Must have
• I will need to have my firms logo "Keystone 8" and my logo "HTR" on the business card. I would like to have my firms logo smaller then mine. I would also like to have my photo on the card. By business colors are gold and white with blue accents.
Nice to have
• It would be nice to have a unique shape or feel (texture) rather then your standard business card. I saw cardly press had metal cards which could be interesting.

```html
<!DOCTYPE html>
<html lang="en">
<head>
<meta charset="utf-8">
<title>Harold The Realtor – Business Card</title>
<link href="https://fonts.googleapis.com/css2?family=Michroma&family=Roboto:wght@400;900&display=swap" rel="stylesheet">
<style>
  :root {
    --backdrop: #c8c8c8;
    --card-black: #151515;
    --card-white: #f4f4f4;
    --card-white-shade: #e2e2e2;
    --gold: #a8844a;
    --gold-light: #caa76a;
    --gold-dark: #7c5c2c;
    --ink: #1d1d1d;
    --photo-top: #d9d6d2;
    --photo-bottom: #3d4b6e;
  }
  * { box-sizing: border-box; margin: 0; padding: 0; }
  html, body { width: 1200px; height: 1138px; overflow: hidden; }
  body { background: var(--backdrop); position: relative; font-family: "Roboto", sans-serif; }

  .card {
    position: absolute;
    width: 620px;
    height: 374px;
    border-radius: 16px;
    overflow: hidden;
  }

  /* Front */
  .card--front { left: 274px; top: 186px; background: var(--card-black); }
  .card--front .gold-edge {
    position: absolute; left: 0; right: 0; bottom: 0; height: 10px;
    background: linear-gradient(90deg, var(--gold-dark), var(--gold-light), var(--gold-dark));
  }
  .brand {
    font-family: "Michroma", sans-serif;
    color: var(--gold);
    font-weight: 400;
    text-align: right;
    line-height: 1;
  }
  .card--front .brand {
    position: absolute; left: 0; right: 0; top: 118px;
    display: flex; flex-direction: column; align-items: center;
  }
  .card--front .brand-mark {
    width: 34px; height: 34px; border-radius: 50%;
    background: var(--gold); margin-bottom: 26px;
  }
  .card--front .brand-name { font-size: 52px; letter-spacing: 1px; }
  .card--front .brand-tag { font-size: 17px; letter-spacing: 6px; margin-top: 10px; }
  .card--front .website {
    position: absolute; left: 0; right: 0; top: 322px;
    text-align: center; color: #e8e8e8; font-size: 16px;
  }

  /* Back */
  .card--back {
    left: 276px; top: 608px;
    background: linear-gradient(180deg, var(--card-white), var(--card-white-shade));
  }
  .card--back .portrait-frame { position: absolute; inset: 0; }
  .card--back .brand {
    position: absolute; right: 26px; top: 36px;
  }
  .card--back .brand-name { font-size: 34px; }
  .card--back .brand-tag { font-size: 12px; letter-spacing: 4px; margin-top: 6px; }
  .name-band {
    position: absolute; left: 262px; right: 0; top: 124px; height: 52px;
    background: linear-gradient(90deg, var(--gold-dark), var(--gold-light) 55%, var(--gold));
    display: flex; align-items: center; padding-left: 42px; gap: 14px;
  }
  .name-band .agent-name { font-weight: 900; font-size: 23px; color: var(--ink); letter-spacing: .5px; }
  .name-band .agent-role { font-size: 16px; color: var(--ink); }
  .firm {
    position: absolute; right: 28px; top: 194px;
    display: flex; align-items: center; gap: 8px;
    font-size: 26px; color: var(--ink);
  }
  .firm-dot { width: 30px; height: 30px; border-radius: 50%; background: #8c1c1c; }
  .contacts { position: absolute; left: 302px; top: 242px; list-style: none; }
  .contacts li {
    display: flex; align-items: center; gap: 14px;
    height: 23.5px; font-size: 16px; color: var(--ink);
  }
  .contacts svg { width: 16px; height: 16px; fill: var(--gold); }
</style>
</head>
<body>

<section class="card card--front">
  <div class="brand">
    <span class="brand-mark"></span>
    <span class="brand-name">Harold</span>
    <span class="brand-tag">THE REALTOR</span>
  </div>
  <p class="website">www.HaroldtheRealtor.com</p>
  <div class="gold-edge"></div>
</section>

<section class="card card--back">
  <svg class="portrait-frame" viewBox="0 0 620 374" width="620" height="374">
    <defs>
      <linearGradient id="portraitTone" x1="0" y1="0" x2="0" y2="1">
        <stop offset="0" stop-color="var(--photo-top)"/>
        <stop offset="0.55" stop-color="#9a7560"/>
        <stop offset="1" stop-color="var(--photo-bottom)"/>
      </linearGradient>
      <linearGradient id="arcGold" x1="0" y1="0" x2="0" y2="1">
        <stop offset="0" stop-color="var(--gold-light)"/>
        <stop offset="0.5" stop-color="var(--gold)"/>
        <stop offset="1" stop-color="var(--gold-dark)"/>
      </linearGradient>
    </defs>
    <path role="img" aria-label="Portrait photo of the agent in a suit"
          d="M0 0 H212 Q290 187 212 374 H0 Z" fill="url(#portraitTone)"/>
    <path d="M212 0 Q290 187 212 374 H222 Q300 187 224 0 Z" fill="url(#arcGold)"/>
  </svg>

  <div class="brand">
    <span class="brand-name">Harold</span>
    <span class="brand-tag">THE REALTOR</span>
  </div>

  <div class="name-band">
    <span class="agent-name">HAL MORGAN</span>
    <span class="agent-role">Broker</span>
  </div>

  <div class="firm">
    <span class="firm-name">Keystone 8</span>
    <span class="firm-dot"></span>
  </div>

  <ul class="contacts">
    <li>
      <svg viewBox="0 0 16 16"><path d="M2 5c0-2 2-3 6-3s6 1 6 3v1h-3V5H5v1H2zM4 7h8l2 7H2z"/></svg>
      206-555-0184
    </li>
    <li>
      <svg viewBox="0 0 16 16"><path d="M4 1h8v4H4zM1 6h14v6h-3v3H4v-3H1zM5 10v4h6v-4z"/></svg>
      206-555-0127
    </li>
    <li>
      <svg viewBox="0 0 16 16"><path d="M1 3h14v10H1zM2.5 4.5 8 9l5.5-4.5v1.6L8 10.5 2.5 6.1z" fill-rule="evenodd"/></svg>
      hal@haroldtherealtor.com
    </li>
    <li>
      <svg viewBox="0 0 16 16"><path d="M8 1a7 7 0 1 0 0 14A7 7 0 0 0 8 1zm-1 1.6V7H3A5.5 5.5 0 0 1 7 2.6zm2 0A5.5 5.5 0 0 1 13 7H9zM3 9h4v4.4A5.5 5.5 0 0 1 3 9zm6 0h4a5.5 5.5 0 0 1-4 4.4z"/></svg>
      www.HaroldtheRealtor.com
    </li>
  </ul>
</section>

</body>
</html>
```